Cafe menu design

Hi there,

We need a editable menu layout and design to match our new cafe call: " Harlow Bean Roasters", we love the ideas of A4 clip board and self print out menu in black and white. ( Example as attached)

We would like the menu can be break down into category easy for customer to flip around and read. ( example as attached)

Category including the following:

- All day breakfast and Sandwich and Toast
- Main (Lunch&Dinner) and Pizza
- Dessert snacks and nibbles
- Hot and Cold Drinks
- Catering menu

Please find our logo and our current menu as attached for your information and convenience.
Updates

Dear Designers, Thank you for your time and submission, Please find our drink menu and logo as attached. Kind Regards,

Target Market(s)

Young family, young Couple, office and corporate staff

Industry/Entity Type

Cafe

Font styles to use
Serif
Sans Serif

```html
<!DOCTYPE html>
<html lang="en">
<head>
<meta charset="utf-8">
<title>Harlow Bean Roasters – Menu Set</title>
<link href="https://fonts.googleapis.com/css2?family=Courier+Prime:wght@400;700&family=Special+Elite&display=swap" rel="stylesheet">
<style>
  :root{
    --backdrop:#a3a3a3;
    --paper:#ffffff;
    --ink:#111111;
    --band:#050505;
    --panel:#ebebec;
    --faint:#dcdcdc;
    --faint-disc:#f3f3f3;
    --card-paper:#f7f7f5;
    --card-black:#151515;
  }
  *{box-sizing:border-box;margin:0;padding:0}
  html,body{width:1200px;height:900px;overflow:hidden}
  body{background:var(--backdrop);position:relative;font-family:"Courier Prime",monospace;color:var(--ink)}

  /* Menu sheet */
  .menu-sheet{position:absolute;left:80px;top:93px;width:464px;height:655px;background:var(--paper)}
  .menu-frame{position:absolute;left:10px;top:10px;width:444px;height:405px;border:1px dotted var(--ink)}
  .brand-watermark{position:absolute;left:0;width:464px;text-align:center;
    font-family:"Courier Prime",monospace;font-weight:700;color:var(--faint);line-height:1;letter-spacing:1px}
  .brand-watermark.top{top:110px;font-size:32px}
  .brand-watermark.bottom{top:340px;font-size:20px}
  .brand-watermark-disc{position:absolute;left:157px;top:160px;width:150px;height:150px;border-radius:50%;background:var(--faint-disc)}
  .column-divider{position:absolute;left:227px;top:159px;width:1px;height:237px;background:var(--ink)}
  .drink-list{position:absolute;top:198px;width:176px;list-style:none;font-weight:700;font-size:8px;line-height:9px}
  .drink-list.left{left:47px}
  .drink-list.right{left:235px;top:196px}
  .drink-item{margin-bottom:6px}
  .drink-row{display:flex;align-items:baseline}
  .drink-row .leader{flex:1;border-bottom:1px dotted var(--ink);margin:0 2px 2px}
  .drink-row .plain{flex:1}
  .category-band{position:absolute;left:0;top:425px;width:464px;height:44px;background:var(--band);
    color:#fff;font-family:"Special Elite","Courier Prime",monospace;font-size:15.5px;display:flex;align-items:center;justify-content:center}
  .category-panel{position:absolute;left:0;top:469px;width:464px;height:186px;background:var(--panel)}

  /* Order info card */
  .order-card{position:absolute;left:698px;top:173px;width:368px;height:207px;background:var(--card-paper);
    padding:49px 0 0 24px;white-space:nowrap}
  .order-card p{display:block}
  .order-card .lead{font-size:11px;line-height:18px;letter-spacing:-0.1px}
  .order-card .strong{font-weight:700;font-size:13.5px;line-height:19px;letter-spacing:0}
  .order-card .note{font-size:8px;line-height:18px;letter-spacing:-0.05px}
  .order-card .headline{font-weight:700;font-size:16.5px;line-height:21px;letter-spacing:-0.2px}
  .order-card .detail{font-size:10px;line-height:17px;letter-spacing:-0.25px}
  .order-card .small{font-size:9.5px;line-height:17px;letter-spacing:-0.8px}

  /* Brand card */
  .brand-card{position:absolute;left:697px;top:531px;width:371px;height:208px;background:var(--card-black);
    display:flex;flex-direction:column;align-items:center;justify-content:center;gap:10px}
  .brand-card .dot{width:34px;height:34px;border-radius:50%;background:#fff}
  .brand-card .name{font-family:"Courier Prime",monospace;font-weight:700;font-size:15px;color:#fff;letter-spacing:1px;text-align:center;line-height:1.2}
</style>
</head>
<body>

<section class="menu-sheet" aria-label="Drinks menu page">
  <div class="menu-frame"></div>
  <div class="brand-watermark-disc"></div>
  <div class="brand-watermark top">HARLOW BEAN</div>
  <div class="brand-watermark bottom">ROASTERS</div>
  <div class="column-divider"></div>

  <ul class="drink-list left">
    <li class="drink-item"><div class="drink-row"><span>Signature iced coffee</span><span class="leader"></span><span>6.0</span></div><div>w/ vanilla ice cream</div></li>
    <li class="drink-item"><div class="drink-row"><span>Iced latte (drip coffee)</span><span class="leader"></span><span>5.0</span></div><div class="drink-row"><span>Vanilla</span><span class="plain"></span><span>+0.7</span></div><div>Caramel</div><div>Hazelnut</div></li>
    <li class="drink-item"><div class="drink-row"><span>Iced long black (non dairy)</span><span class="leader"></span><span>5.0</span></div></li>
    <li class="drink-item"><div class="drink-row"><span>Iced mocha/</span><span class="leader"></span><span>5.5</span></div><div class="drink-row"><span>w/ vanilla ice cream</span><span class="plain"></span><span>+1.0</span></div></li>
    <li class="drink-item"><div class="drink-row"><span>Iced white mocha</span><span class="leader"></span><span>5.5</span></div><div class="drink-row"><span>w/ vanilla ice cream</span><span class="plain"></span><span>+1.0</span></div></li>
    <li class="drink-item"><div class="drink-row"><span>Vintage vanilla cappuccino</span><span class="leader"></span><span>6.5</span></div><div>frappe</div></li>
    <li class="drink-item"><div class="drink-row"><span>Mocha java frappe</span><span class="leader"></span><span>6.5</span></div></li>
    <li class="drink-item"><div class="drink-row"><span>Affogato</span><span class="leader"></span><span>6.5</span></div></li>
  </ul>

  <ul class="drink-list right">
    <li class="drink-item"><div class="drink-row"><span>Signature iced coffee</span><span class="leader"></span><span>6.0</span></div><div>w/ vanilla ice cream</div></li>
    <li class="drink-item"><div class="drink-row"><span>Iced latte (drip coffee)</span><span class="leader"></span><span>5.0</span></div><div class="drink-row"><span>Vanilla</span><span class="plain"></span><span>+0.7</span></div><div>Caramel</div><div>Hazelnut</div></li>
    <li class="drink-item"><div class="drink-row"><span>Iced long black (non dairy)</span><span class="leader"></span><span>5.0</span></div></li>
    <li class="drink-item"><div class="drink-row"><span>Iced mocha/</span><span class="leader"></span><span>5.5</span></div><div class="drink-row"><span>w/ vanilla ice cream</span><span class="plain"></span><span>+1.0</span></div></li>
    <li class="drink-item"><div class="drink-row"><span>Iced white mocha</span><span class="leader"></span><span>5.5</span></div><div class="drink-row"><span>w/ vanilla ice cream</span><span class="plain"></span><span>+1.0</span></div></li>
    <li class="drink-item"><div class="drink-row"><span>Vintage vanilla cappuccino</span><span class="leader"></span><span>6.5</span></div><div>frappe</div></li>
    <li class="drink-item"><div class="drink-row"><span>Mocha java frappe</span><span class="leader"></span><span>6.5</span></div></li>
    <li class="drink-item"><div class="drink-row"><span>Affogato</span><span class="leader"></span><span>6.5</span></div></li>
  </ul>

  <div class="category-band">All day breakfast and Sandwich and Toast</div>
  <div class="category-panel" role="img" aria-label="Space reserved for the breakfast, sandwich and toast items"></div>
</section>

<section class="order-card" aria-label="Ordering information">
  <p class="lead">Please call us on 8012 4470 to place your order.</p>
  <p class="strong">Please allow at least 30mins notice .</p>
  <p class="note">( one day notice for hot canapés, and catering size over 50 people )</p>
  <p class="headline">pre-payment in full is required,</p>
  <p class="detail">please visit us at shop 4, 22 Marlow Street, Eastwood</p>
  <p class="small">for cash orders or call to make phone payment ( 7am-5pm, 7 days)</p>
</section>

<section class="brand-card" aria-label="Brand card">
  <span class="dot"></span>
  <span class="name">HARLOW BEAN<br>ROASTERS</span>
</section>

</body>
</html>
```